Real estate broker business card

Want a modern celan but effective business card for my residential and commercial real estate business. I want the back of the card to advertise my services and to capture business. I have attached the back of my current business card fore ideas

Target Market(s)

home buyers and seller. commercial buyers and sellers

Industry/Entity Type

Real Estate

Contact Information for Business Card

must have my contact information and my photo

Requirements
Must have
• Corla Vintreff
• Owner & Qualifying Broker
• Vintreff Real Estate Services
• 505.718.2947
• corla@vintreffhomes.com
• www.vintreffhomes.com
Nice to have
• metallic
• Business capture text: " Don't buy or lease property without someone looking out for your best interests. I will represent you on your home or investment purchase for FREE!"
• "Home owners, call today to receive a FREE market analysis for your homes value!

```html
<!DOCTYPE html>
<html lang="en">
<head>
<meta charset="utf-8">
<title>Vintreff Real Estate Services – Business Card</title>
<link rel="stylesheet" href="https://fonts.googleapis.com/css2?family=Source+Sans+3:wght@400;600;700&display=swap">
<style>
  :root {
    --teal: #147f8c;
    --teal-deep: #0e6b77;
    --teal-soft: #1a8b98;
    --ink-white: #ffffff;
    --paper: #ffffff;
    --stage: #e9ebec;
    --brand-grey: #5d6468;
    --photo-dark: #2a1d18;
    --photo-light: #e8e4e0;
  }
  * { box-sizing: border-box; margin: 0; padding: 0; }
  html, body {
    width: 1200px; height: 900px; overflow: hidden;
    background: var(--stage);
    font-family: "Source Sans 3", "Myriad Pro", Arial, sans-serif;
  }
  .canvas { position: relative; width: 1200px; height: 900px; }

  /* Front */
  .card-front {
    position: absolute; left: 78px; top: 35px;
    width: 588px; height: 363px;
    background: var(--paper); overflow: hidden;
    box-shadow: 0 6px 18px rgba(0,0,0,.18);
  }
  .front-band {
    position: absolute; left: 0; top: 181px; width: 100%; height: 182px;
    background: var(--teal);
  }
  .brand {
    position: absolute; left: 32px; top: 72px;
    display: flex; align-items: center; gap: 14px;
  }
  .brand-mark {
    width: 52px; height: 52px; border-radius: 50%;
    background: linear-gradient(135deg, var(--teal-soft), var(--teal-deep));
  }
  .brand-name {
    color: var(--teal); font-weight: 600;
    font-size: 27px; line-height: 1.05; letter-spacing: .5px;
    text-transform: uppercase; width: 250px;
  }
  .agent {
    position: absolute; left: 31px; top: 208px; color: var(--ink-white);
  }
  .agent-name { font-size: 20px; font-weight: 600; line-height: 1.1; }
  .agent-title { font-size: 16px; font-weight: 400; margin-top: 2px; }
  .contacts {
    position: absolute; left: 31px; top: 274px;
    list-style: none; color: var(--ink-white); font-size: 16px;
  }
  .contacts li { display: flex; align-items: center; gap: 9px; height: 21px; }
  .contacts svg { width: 13px; height: 13px; fill: var(--ink-white); flex: none; }
  .portrait {
    position: absolute; right: 0; top: 0; width: 250px; height: 363px;
    background:
      radial-gradient(ellipse 60% 45% at 55% 38%, #c99f87 0 40%, transparent 70%),
      linear-gradient(180deg, var(--photo-dark) 0 55%, var(--photo-light) 75%);
    clip-path: polygon(18% 0, 100% 0, 100% 100%, 0 100%, 6% 70%, 2% 45%, 8% 20%);
  }

  /* Back */
  .card-back {
    position: absolute; left: 388px; top: 505px;
    width: 567px; height: 352px; overflow: hidden;
    background: linear-gradient(90deg, var(--teal-soft), var(--teal) 50%, var(--teal-deep));
    box-shadow: 0 6px 18px rgba(0,0,0,.18);
  }
  .back-watermark {
    position: absolute; left: -10px; top: -20px; width: 620px;
    color: rgba(255,255,255,.07); font-weight: 600;
    font-size: 118px; line-height: 1.45; letter-spacing: 4px;
    text-transform: uppercase; white-space: nowrap;
  }
  .pitch {
    position: absolute; left: 0; top: 71px; width: 100%;
    text-align: center; color: var(--ink-white);
    font-weight: 600; font-size: 17.5px; line-height: 30.5px;
    text-transform: uppercase; letter-spacing: .2px;
  }
  .pitch p + p { margin-top: 30px; }
</style>
</head>
<body>
<main class="canvas">

  <section class="card-front" aria-label="Business card front">
    <div class="front-band"></div>

    <div class="brand">
      <span class="brand-mark"></span>
      <span class="brand-name">Vintreff Real Estate Services</span>
    </div>

    <div class="agent">
      <h1 class="agent-name">Corla Vintreff</h1>
      <p class="agent-title">Owner &amp; Qualifying Broker</p>
    </div>

    <ul class="contacts">
      <li>
        <svg viewBox="0 0 24 24" aria-hidden="true"><path d="M6.6 10.8a15 15 0 0 0 6.6 6.6l2.2-2.2a1 1 0 0 1 1-.25 11.4 11.4 0 0 0 3.6.6 1 1 0 0 1 1 1V20a1 1 0 0 1-1 1A17 17 0 0 1 3 4a1 1 0 0 1 1-1h3.5a1 1 0 0 1 1 1c0 1.25.2 2.45.6 3.6a1 1 0 0 1-.25 1z"/></svg>
        505.718.2947
      </li>
      <li>
        <svg viewBox="0 0 24 24" aria-hidden="true"><path d="M2 5h20v14H2z" fill="none"/><path d="M2 5h20v14H2V5zm2 2v.5l8 5 8-5V7H4z"/></svg>
        corla@vintreffhomes.com
      </li>
      <li>
        <svg viewBox="0 0 24 24" aria-hidden="true"><circle cx="12" cy="12" r="10"/><path d="M7 9l4 2-1 4 3 3 1-5 3-2-3-3-3 2z" fill="var(--teal)"/></svg>
        www.vintreffhomes.com
      </li>
    </ul>

    <div class="portrait" role="img" aria-label="Portrait photo of the broker"></div>
  </section>

  <section class="card-back" aria-label="Business card back">
    <div class="back-watermark" aria-hidden="true">Vintreff<br>Vintreff</div>
    <div class="pitch">
      <p>Don't buy or lease property without someone<br>looking out for your best interests.<br>I will represent you on your home or<br>investment purchase for free!</p>
      <p>Home owners, call today to receive a free market<br>analysis for your homes value!</p>
    </div>
  </section>

</main>
</body>
</html>
```